New south Australia high-end red wine label & logo design

Marvel Ridge Estate exports premium south Australian wine to oversea market. We are looking for a professional graphic designer to design a full set of wine label and logo for our new red wine, the label & logo should look 'high-end' & Luxury and attractive. Black & gold color is preferred. I have attached example images to demonstrate the feel that we are looking for. These are just a possible starting point. The expectation is that the label would be professional/polished. I am open to any and all designs that would alter my perception of what will be best!

Target customer -

we need the label to be print-ready.

There will be 3 parts to this design.

Top Cover design with gold text wrapped, the front label and the back label

-Brand name Marvin Estate
-text wine of Australia
-text Cabernet
-Year 2015
-text Sourced from premium Australian wine growing region Kelmarsh valley

Look and Feel:
• Elegant
• Serious
• Modern/Traditional
• Professional
• Gender Neutral
• Upmarket

--------------Back Label text---------------
Rich and opulent with intense fruit aromas of black berry, liquorice and cassis with hints of dark chocolate and pungent spices. Sumptuous and textured palate with beautifully detailed ripe black fruits flowing seamlessly across the palate. French oak provides a complex harmony and finish of great length, balance and purity.

Produced by Kova Lindquist Holdings International Pty Ltd
27 Felbrook Lane,Norvale, South Australia, 5172
14.5 ALC/VOL
Wine of Australia
Approx 8.3 Standard Drinks
Contains Sulphites
750 ML
Please leave the space for Bar Code

Requirements
Must have
• wine name, wine logo, wine type etc (should include all 'must-have the required fields wine lable)
Nice to have
• Desginer's own idea
Should not have
• should not be too playful

```html
<!DOCTYPE html>
<html lang="en">
<head>
<meta charset="utf-8">
<title>Marvin Estate – Cabernet Front Label</title>
<link rel="stylesheet" href="https://fonts.googleapis.com/css2?family=Cinzel:wght@400;500&family=Cormorant+Garamond:wght@500&family=Pinyon+Script&display=swap">
<style>
  :root {
    --page-bg: #1c1c1c;
    --label-bg: #1a1a1a;
    --gold: #b8962e;
    --gold-light: #d9bd6a;
    --ivory: #ece6d6;
    --emblem-dark: #101010;
    --emblem-mid: #2a2a2a;
  }
  html, body {
    margin: 0;
    padding: 0;
    width: 1130px;
    height: 1200px;
    overflow: hidden;
    background: var(--page-bg);
  }
  .canvas {
    position: relative;
    width: 1130px;
    height: 1200px;
  }
  .front-label {
    position: absolute;
    left: 120px;
    top: 60px;
    width: 890px;
    height: 1080px;
    box-sizing: border-box;
    background: var(--label-bg);
    border: 7px solid var(--gold);
  }
  .crest-artwork {
    position: absolute;
    left: 230px;
    top: 50px;
    width: 420px;
    height: 420px;
    background: radial-gradient(ellipse at 50% 50%, var(--emblem-mid) 0%, var(--emblem-dark) 55%, var(--label-bg) 75%);
  }
  .vintage {
    position: absolute;
    left: 278px;
    top: 468px;
    margin: 0;
    font-family: "Cormorant Garamond", serif;
    font-variant-numeric: oldstyle-nums;
    font-weight: 500;
    font-size: 44px;
    letter-spacing: 6px;
    color: var(--ivory);
  }
  .brand-name {
    position: absolute;
    left: 0;
    right: 0;
    top: 625px;
    margin: 0;
    text-align: center;
    font-family: "Pinyon Script", cursive;
    font-weight: 400;
    font-size: 112px;
    line-height: 1;
    color: var(--gold-light);
  }
  .varietal {
    position: absolute;
    left: 0;
    right: 0;
    top: 766px;
    display: flex;
    justify-content: center;
    align-items: center;
    gap: 26px;
    font-family: "Cinzel", serif;
    font-size: 22px;
    letter-spacing: 16px;
    color: var(--ivory);
  }
  .varietal::before,
  .varietal::after {
    content: "";
    width: 60px;
    height: 2px;
    background: var(--ivory);
  }
  .brand-square {
    position: absolute;
    left: 410px;
    top: 832px;
    width: 56px;
    height: 76px;
    box-sizing: border-box;
    border: 3px solid #0c0c0c;
    background: #141414;
  }
  .provenance {
    position: absolute;
    left: 0;
    right: 0;
    top: 940px;
    margin: 0;
    text-align: center;
    font-family: "Cinzel", serif;
    font-size: 15px;
    line-height: 21px;
    letter-spacing: 4px;
    color: var(--ivory);
  }
  .region {
    position: absolute;
    left: 0;
    right: 0;
    top: 1004px;
    margin: 0;
    text-align: center;
    font-family: "Cinzel", serif;
    font-weight: 500;
    font-size: 38px;
    letter-spacing: 2px;
    color: var(--ivory);
  }
</style>
</head>
<body>
  <main class="canvas">
    <section class="front-label">
      <div class="crest-artwork" role="img" aria-label="Embossed black griffin crest illustration"></div>
      <p class="vintage">2015</p>
      <h1 class="brand-name">Marvin Estate</h1>
      <div class="varietal">CABERNET</div>
      <div class="brand-square"></div>
      <p class="provenance">SOURCED FROM<br>PREMIUM AUSTRALIAN<br>WINE GROWING REGION</p>
      <p class="region">KELMARSH VALLEY</p>
    </section>
  </main>
</body>
</html>
```